HomePage Design for Lumen Getaways - once-in-a-lifetime experiences for busy working people

Design a homepage for the Lumen Getaways (www.lumengetaways.example) website compatible with further web pages and the design briefing documents attached

LG HomePage Design Brief
We are seeking website HomePage designs incorporating our new Logo and colour scheme, for Lumen Getaways (www.lumengetaways.example) to go with the site functionality and wireframe ideas attached.
The website HomePage design needs to
• Incorporate and be consistent with the LG Logo and its colour scheme attached.
• Express the brand values of being inspirational, high quality, upscale, cultured, aspirational, and contemporary – even somewhat ‘hip’. Probably positioned somewhere between Harlow Pike (Deluxe Travel) and Green Walrus (Hip Travel) – see https://www.harlowpike.example and https://www.greenwalrus.example .
• Be instantly recognisable and different from other travel websites and instantly communicate the nature of the brand proposition and target customer base.
• Appeal to our core 25-55 affluent businesspeople demographic
• Work in the UK, US/Canada and Australia/NZ and ultimately in mainland Europe.
• Use fonts and colours that are easily reproduced online and compatible with nearly all browsers.
• Be part of a responsive website design, that can be used both on Desktops and laptops but also with tablets and mobile ‘phones (hence content not too wide across the page)
• Feature the strapline ‘Lumen Getaways in less than 7 Days’
• Work with the and wireframes and processes shown in the attached presentation – although intended as a guide only these features and processes all need to be incorporated into the HomePage.
• Make full use of high quality images and video to convey our brand proposition and products

Target Market(s)

25-55 affluent businesspeople

Industry/Entity Type

Travel Industry

Number of Pages Required

1 page

Font styles to use
Sans Serif

Colors
0455a3
00a88f

Requirements
Must have
• • Incorporate and be consistent with the LG Logo and its colour scheme attached.
• • Express the brand values of being inspirational, high quality, upscale, cultured, aspirational, and contemporary – even somewhat ‘hip’. Probably positioned somewhere between Harlow Pike (Deluxe Travel) and Green Walrus (Hip Travel) – see https://www.harlowpike.example and https://www.greenwalrus.example .
• • Be instantly recognisable and different from other travel websites and instantly communicate the nature of the brand proposition and target customer base.
• • Appeal to our core 25-55 affluent businesspeople demographic
• • Be part of a responsive website design, that can be used both on Desktops and laptops but also with tablets and mobile ‘phones (hence content not too wide across the page)
• • Feature the strapline ‘Lumen Getaways in less than 7 Days’
• • Work with the and wireframes and processes shown in the attached presentation – although intended as a guide only these features and processes all need to be incorporated into the HomePage.
• • Make full use of high quality images and video to convey our brand proposition and products
• Colours as per Logo not as shown below
Nice to have
• • Work in the UK, US/Canada and Australia/NZ and ultimately in mainland Europe.
Should not have
• Must not be cheap or mass-market, nor excessively "stuffy or luxury-orientated"

```html
<!DOCTYPE html>
<html lang="en">
<head>
<meta charset="utf-8">
<title>Lumen Getaways – Home</title>
<link rel="stylesheet" href="https://fonts.googleapis.com/css2?family=Chewy&family=Poppins:wght@500;600&family=Roboto:wght@400;500;700&display=swap">
<style>
  :root{
    --navy:#0455a3;
    --ink:#1f2a44;
    --teal:#00a88f;
    --text:#222629;
    --page:#f5f5f5;
    --white:#ffffff;
    --rule:#e4e4e4;
    --footer:#282c3a;
    --footer-text:#d9dbe2;
    --footer-rule:#363b4b;
  }
  *{box-sizing:border-box;margin:0;padding:0}
  html,body{width:1200px;height:2244px;overflow:hidden}
  body{position:relative;background:var(--white);font-family:"Roboto",Arial,sans-serif;color:var(--text)}

  /* header */
  .site-header{position:absolute;left:0;top:0;width:1200px;height:90px;background:var(--white)}
  .brand{position:absolute;left:90px;top:28px;display:flex;align-items:center;gap:10px}
  .brand-dot{width:30px;height:30px;border-radius:50%;background:var(--teal)}
  .brand-name{font-family:"Poppins",Arial,sans-serif;font-weight:600;font-size:17px;color:var(--navy);letter-spacing:.3px}
  .follow{position:absolute;left:860px;top:33px;display:flex;align-items:center;gap:11px}
  .follow-label{font-size:11.5px;font-weight:500;color:var(--text);margin-right:10px;letter-spacing:.2px}
  .social{width:24px;height:24px;border-radius:50%;background:var(--navy)}
  .social:nth-of-type(even){background:var(--teal)}

  /* hero */
  .hero{position:absolute;left:0;top:90px;width:1200px;height:534px;
    background:radial-gradient(ellipse 38% 55% at 52% 52%,#2aa7c4 0%,#1a86a8 55%,rgba(26,134,168,0) 100%),
               linear-gradient(100deg,#2d4a25 0%,#3c6130 28%,#5c7a44 50%,#7a8a5c 70%,#4d6a38 100%)}
  .hero-title{position:absolute;left:0;width:1200px;text-align:center;color:var(--white)}
  .hero-kicker{top:226px;font-family:"Poppins",Arial,sans-serif;font-weight:600;font-size:25px}
  .hero-line{top:253px;font-family:"Chewy","Poppins",cursive;font-size:44px;letter-spacing:.5px}
  .hero-arrow{position:absolute;top:338px;width:30px;height:42px;display:flex;align-items:center;justify-content:center}
  .hero-arrow.prev{left:6px}
  .hero-arrow.next{right:0;background:var(--white)}
  .scroll-cue{position:absolute;left:588px;top:472px}

  /* nav */
  .main-nav{position:absolute;left:0;top:624px;width:1200px;height:61px;background:var(--white);border-bottom:1px solid var(--rule)}
  .main-nav a{position:absolute;top:24px;font-size:12px;font-weight:500;color:var(--text);text-decoration:none;text-transform:uppercase;letter-spacing:.2px}
  .main-nav a.active{color:var(--teal)}
  .nav-underline{position:absolute;left:102px;top:681px;width:52px;height:3px;background:var(--teal)}

  /* content */
  .content{position:absolute;left:0;top:685px;width:1200px;height:1219px;background:var(--page)}
  .section-title{position:absolute;top:66px;font-family:"Poppins",Arial,sans-serif;font-weight:500;font-size:23px;color:var(--text)}
  .section-title::after{content:"";position:absolute;left:0;top:38px;width:30px;height:2px;background:#c9c9c9}
  .tile{position:absolute;width:341px;height:234px;overflow:hidden}
  .tile::after{content:"";position:absolute;left:0;right:0;bottom:0;height:90px;background:linear-gradient(rgba(0,0,0,0),rgba(0,0,0,.38))}
  .tile-label{position:absolute;left:0;right:0;bottom:18px;text-align:center;color:var(--white);font-size:16px;font-weight:500;z-index:1}
  .play{position:absolute;left:144px;top:90px;z-index:1}

  .place{position:absolute;left:153px;width:273px;height:213px}
  .place-tag{position:absolute;left:0;top:193px;width:229px;height:42px;background:var(--teal);color:var(--white);font-size:15px;font-weight:500;padding:12px 0 0 18px}

  /* footer */
  .site-footer{position:absolute;left:0;top:1904px;width:1200px;height:340px;background:var(--footer);color:var(--footer-text)}
  .footer-col{position:absolute;top:72px;list-style:none}
  .footer-col li{position:relative;font-size:12px;line-height:15px;margin-bottom:20px;padding-left:12px}
  .footer-col li::before{content:"";position:absolute;left:0;top:6px;width:3px;height:3px;border-radius:50%;background:#8a8fa0}
  .footer-divider{position:absolute;top:56px;width:1px;height:206px;background:var(--footer-rule)}
  .copyright{position:absolute;left:93px;top:294px;font-size:12px}
  .payments{position:absolute;left:875px;top:285px;display:flex;gap:10px}
  .pay-card{width:52px;height:34px;border-radius:4px;background:#f1f2f5}
  .pay-card.dark{background:#2234a0}
  .pay-card.black{background:#15161a}
  .to-top{position:absolute;left:1139px;top:245px;width:34px;height:34px;border-radius:50%;background:var(--teal);display:flex;align-items:center;justify-content:center}
</style>
</head>
<body>

<header class="site-header">
  <div class="brand"><span class="brand-dot"></span><span class="brand-name">Lumen Getaways</span></div>
  <div class="follow">
    <span class="follow-label">FOLLOW US:</span>
    <span class="social"></span><span class="social"></span><span class="social"></span><span class="social"></span><span class="social"></span>
  </div>
</header>

<section class="hero" role="img" aria-label="Paraglider soaring over a turquoise lagoon with forested hills and a sandy beach">
  <p class="hero-title hero-kicker">Lumen Getaways</p>
  <p class="hero-title hero-line">is an online Marketplace</p>
  <span class="hero-arrow prev"><svg width="10" height="14" viewBox="0 0 10 14"><path d="M7 2 2 7l5 5" fill="none" stroke="#fff" stroke-width="2"/></svg></span>
  <span class="hero-arrow next"><svg width="10" height="14" viewBox="0 0 10 14"><path d="M3 2l5 5-5 5" fill="none" stroke="#222" stroke-width="2"/></svg></span>
  <svg class="scroll-cue" width="22" height="34" viewBox="0 0 22 34"><rect x="1.5" y="1.5" width="19" height="31" rx="9.5" fill="none" stroke="#fff" stroke-width="2"/><line x1="11" y1="8" x2="11" y2="14" stroke="#fff" stroke-width="2" stroke-linecap="round"/></svg>
</section>

<nav class="main-nav">
  <a class="active" style="left:112px">Home</a>
  <a style="left:180px">Destinations</a>
  <a style="left:296px">Experiences</a>
  <a style="left:408px">Trips by Month</a>
  <a style="left:540px">Topical Now</a>
  <a style="left:652px">Tailored</a>
  <a style="left:741px">Pioneers Club</a>
  <a style="left:865px">Client Log-in</a>
  <a style="left:980px">Vlogs &amp; Reviews</a>
</nav>
<span class="nav-underline"></span>

<main class="content">
  <h2 class="section-title" style="left:90px">Lumen Getaways in less than 7 Days!</h2>

  <div class="tile" style="left:88px;top:130px;background:linear-gradient(160deg,#d9dcd8,#8c8e80 45%,#4e5a3e)" role="img" aria-label="Stag standing in a snowy forest clearing"><span class="tile-label">Wonders of Wildlife</span></div>
  <div class="tile" style="left:455px;top:130px;background:radial-gradient(ellipse at 50% 10%,#e7a866,#8a4a25 45%,#2b1610)" role="img" aria-label="Crowd with raised hands at a festival stage"><span class="tile-label">World's Greatest Festivals</span></div>

  <div class="tile" style="left:88px;top:392px;background:linear-gradient(170deg,#5c6a3a,#6f7b45 50%,#4a4030)" role="img" aria-label="Husky team pulling a musher on a forest trail"><span class="tile-label">Must Do Activities</span></div>
  <div class="tile" style="left:455px;top:392px;background:linear-gradient(180deg,#3d6aa8,#7f8fb0 45%,#e0945a 75%,#5c4a3c)" role="img" aria-label="Hot air balloons rising at sunrise over rocky valleys"><span class="tile-label">Unique Annual Events</span></div>

  <div class="tile" style="left:88px;top:654px;background:linear-gradient(180deg,#b9cde0,#7d8ea0 40%,#4f6a5a 75%,#3b4a3a)" role="img" aria-label="Mountain lake beneath snow-capped peaks"><span class="tile-label">Extraordinary &amp; Secret Places</span></div>
  <div class="tile" style="left:455px;top:654px;background:linear-gradient(180deg,#5e5f63,#8d8580 50%,#b6a08a)" role="img" aria-label="Ballet dancers performing on a beach at dusk"><span class="tile-label">Unforgettable Performances</span></div>

  <div class="tile" style="left:88px;top:914px;background:linear-gradient(180deg,#c8ccd2,#e6e8ec 50%,#9ea3aa)" role="img" aria-label="Two hikers walking through snow"><span class="tile-label">Spectacular Hiking, Climbing &amp; Walking</span></div>
  <div class="tile" style="left:455px;top:914px;background:linear-gradient(160deg,#6b6f74,#a6a49c 50%,#cfc6b8)" role="img" aria-label="Skydivers in freefall, video preview">
    <svg class="play" width="54" height="54" viewBox="0 0 54 54"><circle cx="27" cy="27" r="27" fill="#fff"/><path d="M22 18l14 9-14 9z" fill="#111"/></svg>
    <span class="tile-label">Watch A Video Play</span>
  </div>

  <h2 class="section-title" style="left:836px">Last Few Places</h2>
  <div style="position:absolute;left:685px;top:0">
    <div class="place" style="top:130px;background:linear-gradient(150deg,#3d6a3c,#4fa0d0 50%,#2e77b0)" role="img" aria-label="Masked carnival costume in blue and white"><span class="place-tag">Venice Carnival £599pp</span></div>
    <div class="place" style="top:392px;background:linear-gradient(180deg,#1f5ad0,#4e86e0 55%,#5a7a4a)" role="img" aria-label="Stone statues under a blue sky"><span class="place-tag">Easter Island £2,999pp</span></div>
    <div class="place" style="top:652px;background:linear-gradient(160deg,#d8d8d8,#9a9a9a 50%,#3a3a3a)" role="img" aria-label="Costumed figure holding marigolds at a street celebration"><span class="place-tag">Day of the Dead £3,299pp</span></div>
  </div>
</main>

<footer class="site-footer">
  <ul class="footer-col" style="left:175px"><li>About</li><li>Our Partners</li><li>Newsletter</li><li>FAQs</li></ul>
  <span class="footer-divider" style="left:344px"></span>
  <ul class="footer-col" style="left:411px"><li>Contact us</li><li>Booking Conditions</li><li>Privacy &amp; Cookies</li><li>Terms of Use</li></ul>
  <span class="footer-divider" style="left:601px"></span>
  <ul class="footer-col" style="left:667px"><li>Financial Protection</li><li>Travel Insurance</li><li>Visas</li><li>Travel Advice</li></ul>
  <span class="footer-divider" style="left:857px"></span>
  <ul class="footer-col" style="left:883px"><li style="margin-bottom:18px">LG Protecting Wildlife &amp; Animals,<br>and supporting local communities</li><li>Press Room</li></ul>
  <p class="copyright">© Copyright 2017 &nbsp;|&nbsp; All Rights Reserved</p>
  <div class="payments"><span class="pay-card"></span><span class="pay-card dark"></span><span class="pay-card black"></span><span class="pay-card"></span></div>
  <span class="to-top"><svg width="10" height="7" viewBox="0 0 10 7"><path d="M1 6l4-4 4 4" fill="none" stroke="#fff" stroke-width="1.8"/></svg></span>
</footer>

</body>
</html>
```